Letterhead

We are looking for a basic letterhead. It should include our logo, website - northpeakkitchenware.com, phone 907.418.3952, toll free 855.392.6180, and fax 907.418.5263, along with our address 4837 Birchwood Lane, Anchorage, AK 99517. I want something that will look good printed in color or black and white.

```html
<!DOCTYPE html>
<html lang="en">
<head>
<meta charset="utf-8">
<title>North Peak Kitchenware Letterhead</title>
<link rel="stylesheet" href="https://fonts.googleapis.com/css2?family=Montserrat:wght@600;700&display=swap">
<style>
  :root {
    --brand-blue: #1d3e7c;
    --brand-red: #c8374a;
    --ink: #111111;
    --paper: #ffffff;
  }
  html, body {
    margin: 0;
    padding: 0;
    overflow: hidden;
    background: var(--paper);
  }
  .letterhead {
    position: relative;
    width: 849px;
    height: 1200px;
    background: var(--paper);
    font-family: "Montserrat", Arial, sans-serif;
    color: var(--ink);
    overflow: hidden;
  }
  .brand {
    position: absolute;
    left: 47px;
    top: 96px;
    margin: 0;
    display: flex;
    align-items: center;
    gap: 12px;
  }
  .brand__mark {
    width: 16px;
    height: 16px;
    background: var(--brand-red);
  }
  .brand__name {
    font-size: 21px;
    font-weight: 700;
    color: var(--ink);
    line-height: 1;
  }
  .header-rule {
    position: absolute;
    left: 286px;
    right: 0;
    top: 137px;
    height: 10px;
    background: var(--brand-red);
  }
  .header-rule--thin {
    top: 150px;
    height: 2px;
    background: var(--brand-blue);
  }
  .contact-line {
    position: absolute;
    right: 18px;
    top: 166px;
    margin: 0;
    font-size: 11.5px;
    font-weight: 600;
  }
  .footer-rule {
    position: absolute;
    left: 51px;
    width: 749px;
    top: 1097px;
    height: 1px;
    background: var(--brand-red);
  }
  .footer-address {
    position: absolute;
    left: 78px;
    top: 1113px;
    margin: 0;
    font-size: 11.5px;
    font-weight: 700;
  }
  .footer-web {
    position: absolute;
    left: 531px;
    top: 1113px;
    margin: 0;
    font-size: 11.5px;
    font-weight: 600;
    display: flex;
    align-items: center;
    gap: 11px;
  }
  .footer-web__dot {
    width: 7px;
    height: 7px;
    border-radius: 50%;
    background: var(--ink);
  }
</style>
</head>
<body>
  <main class="letterhead">
    <header>
      <h1 class="brand">
        <span class="brand__mark"></span>
        <span class="brand__name">North Peak Kitchenware</span>
      </h1>
      <div class="header-rule"></div>
      <div class="header-rule header-rule--thin"></div>
      <p class="contact-line">Phone : 907.418.3952, Toll free : 855.392.6180, Fax : 907.418.5263</p>
    </header>
    <footer>
      <div class="footer-rule"></div>
      <p class="footer-address">Address : 4837 Birchwood Lane, Anchorage, AK 99517</p>
      <p class="footer-web"><span class="footer-web__dot"></span>www.northpeakkitchenware.com</p>
    </footer>
  </main>
</body>
</html>
```